Talvex Industrial Maintenance Business Card

Design a business card with the following information, logo must be included.
Talvex Industrial Maintenance
Dale Virnow Jr.
Pone 413-627-8154
email dale.virnow.jr@brindlemail.net

```html
<!DOCTYPE html>
<html lang="en">
<head>
<meta charset="utf-8">
<title>Talvex Industrial Maintenance – Business Card</title>
<link href="https://fonts.googleapis.com/css2?family=Montserrat:wght@400;500;600;700&display=swap" rel="stylesheet">
<style>
  :root {
    --brand-blue: #1a72b9;
    --card-white: #ffffff;
    --ink: #1b1b1b;
    --icon-grey: #8a8a8a;
    --backdrop: #8c8c8c;
  }
  * { box-sizing: border-box; margin: 0; padding: 0; }
  html, body { width: 1200px; height: 1017px; overflow: hidden; }
  body {
    background: var(--backdrop);
    font-family: "Montserrat", sans-serif;
    display: flex;
    flex-direction: column;
    align-items: center;
    justify-content: center;
    gap: 64px;
  }
  .card {
    width: 700px;
    height: 400px;
    position: relative;
    box-shadow: 0 10px 30px rgba(0,0,0,0.25);
    overflow: hidden;
  }
  .card--front {
    background: var(--brand-blue);
    display: flex;
    align-items: center;
    justify-content: center;
    gap: 28px;
    color: var(--card-white);
  }
  .brand-dot {
    width: 92px;
    height: 92px;
    border-radius: 50%;
    background: var(--card-white);
    flex: none;
  }
  .brand-name { font-weight: 600; line-height: 1; }
  .brand-name__main { display: block; font-size: 78px; letter-spacing: 1px; }
  .brand-name__sub { display: block; font-size: 20.5px; letter-spacing: 1px; margin-top: 8px; }

  .card--back {
    background: var(--card-white);
    display: flex;
    align-items: center;
    padding: 0 56px;
  }
  .back-brand {
    display: flex;
    align-items: center;
    gap: 16px;
    color: var(--brand-blue);
    width: 250px;
  }
  .back-brand .brand-dot { width: 56px; height: 56px; background: var(--brand-blue); }
  .back-brand .brand-name { font-size: 40px; }
  .divider {
    width: 2px;
    height: 140px;
    background: var(--brand-blue);
    margin: 0 44px 0 16px;
  }
  .contact__name {
    font-size: 38px;
    font-weight: 700;
    color: var(--brand-blue);
    margin-bottom: 14px;
  }
  .contact__line {
    display: flex;
    align-items: center;
    gap: 12px;
    font-size: 16px;
    color: var(--ink);
    margin-top: 6px;
  }
  .contact__line svg { width: 16px; height: 16px; flex: none; fill: var(--icon-grey); }
</style>
</head>
<body>
  <section class="card card--front">
    <div class="brand-dot"></div>
    <div class="brand-name">
      <span class="brand-name__main">TALVEX</span>
      <span class="brand-name__sub">INDUSTRIAL MAINTENANCE</span>
    </div>
  </section>

  <section class="card card--back">
    <div class="back-brand">
      <div class="brand-dot"></div>
      <div class="brand-name">Talvex</div>
    </div>
    <div class="divider"></div>
    <div class="contact">
      <p class="contact__name">Dale Virnow Jr.</p>
      <p class="contact__line">
        <svg viewBox="0 0 24 24" aria-hidden="true"><path d="M6.6 10.8c1.4 2.8 3.8 5.1 6.6 6.6l2.2-2.2c.3-.3.7-.4 1-.2 1.1.4 2.3.6 3.6.6.6 0 1 .4 1 1V20c0 .6-.4 1-1 1C10.6 21 3 13.4 3 4c0-.6.4-1 1-1h3.5c.6 0 1 .4 1 1 0 1.3.2 2.5.6 3.6.1.3 0 .7-.2 1l-2.3 2.2z"/></svg>
        413-627-8154
      </p>
      <p class="contact__line">
        <svg viewBox="0 0 24 24" aria-hidden="true"><path d="M2 5h20v14H2z M4 7v.4l8 5.2 8-5.2V7z" fill-rule="evenodd"/></svg>
        dale.virnow.jr@brindlemail.net
      </p>
    </div>
  </section>
</body>
</html>
```